General contractor/GM consaltant business card

I need a card for my contracting company in North Dakota, we build industrial buildings for the oil feild and oil feild related companies offices, shops, airplain hangars, airports ext. We have a familly atmosphere on the job and are very relational and personal.
Industry/Entity Type
Industrial
Contact Information for Business Card
Kestrelmoor Builders LLC.
Dwight T.Halvorsun
4736 Quillfern dr. Colorado Springs, CO. 80927
Cell# 406-555-8142
dwight@kestrelmoorbuilders.com

```html
<!DOCTYPE html>
<html lang="en">
<head>
<meta charset="utf-8">
<title>Kestrelmoor Builders LLC. — Business Card</title>
<link href="https://fonts.googleapis.com/css2?family=Josefin+Sans:wght@300;400&display=swap" rel="stylesheet">
<style>
  :root {
    --stage: #2b2a29;
    --card-grey: #5f5f5f;
    --card-white: #f4f4f2;
    --ink: #5a5a5a;
    --name-white: #f2f2f2;
  }
  * { margin: 0; padding: 0; box-sizing: border-box; }
  html, body {
    width: 1200px; height: 1200px; overflow: hidden;
    background: var(--stage);
    font-family: "Josefin Sans", sans-serif;
  }
  .stage {
    width: 1200px; height: 1200px;
    display: flex; flex-direction: column;
    align-items: center; justify-content: center; gap: 60px;
  }
  .card {
    position: relative;
    width: 700px; height: 400px;
    overflow: hidden;
    box-shadow: 0 8px 24px rgba(0,0,0,.45);
  }

  /* Contact side */
  .card--contact { background: var(--card-white); }
  .contact-header {
    position: absolute; left: 0; top: 0; width: 100%; height: 150px;
    background: var(--card-grey);
    display: flex; flex-direction: column; justify-content: center; align-items: center;
  }
  .contact-stripe {
    position: absolute; left: 0; width: 100%; background: var(--card-grey);
  }
  .contact-stripe--one { top: 162px; height: 8px; }
  .contact-stripe--two { top: 180px; height: 8px; }
  .contact-list {
    position: absolute; left: 60px; top: 212px;
    list-style: none;
    color: var(--ink); font-weight: 300; font-size: 24px;
  }
  .contact-list li {
    display: flex; align-items: center; gap: 12px;
    height: 40px;
  }
  .contact-list svg { width: 20px; height: 20px; fill: var(--ink); flex: none; }

  /* Company name (shared) */
  .company-name {
    color: var(--name-white); font-weight: 300; text-align: center;
    text-transform: uppercase; line-height: 1;
  }
  .company-name__main { display: block; font-size: 66px; letter-spacing: 4px; }
  .company-name__sub { display: block; font-size: 28px; letter-spacing: 8px; margin-top: 10px; }

  /* Front side */
  .card--front { background: var(--card-grey); }
  .front-name {
    position: absolute; left: 0; top: 90px; width: 100%;
  }
  .front-stripe {
    position: absolute; left: 0; width: 100%; background: var(--card-white);
  }
  .front-stripe--one { top: 312px; height: 7px; }
  .front-stripe--two { top: 330px; height: 7px; }
</style>
</head>
<body>
<main class="stage">

  <section class="card card--contact" aria-label="Business card, contact side">
    <header class="contact-header">
      <p class="company-name">
        <span class="company-name__main">Kestrelmoor</span>
        <span class="company-name__sub">Builders LLC.</span>
      </p>
    </header>
    <div class="contact-stripe contact-stripe--one"></div>
    <div class="contact-stripe contact-stripe--two"></div>
    <ul class="contact-list">
      <li>
        <svg viewBox="0 0 20 20" aria-hidden="true"><circle cx="10" cy="6" r="4.5"/><path d="M2 19c0-5 3.5-7.5 8-7.5s8 2.5 8 7.5z"/></svg>
        Dwight T.Halvorsun
      </li>
      <li>
        <svg viewBox="0 0 20 20" aria-hidden="true"><path d="M10 1a6.5 6.5 0 0 0-6.5 6.5C3.5 12.5 10 19 10 19s6.5-6.5 6.5-11.5A6.5 6.5 0 0 0 10 1zm0 9a2.6 2.6 0 1 1 0-5.2 2.6 2.6 0 0 1 0 5.2z"/></svg>
        4736 Quillfern dr. Colorado Springs, CO. 80927
      </li>
      <li>
        <svg viewBox="0 0 20 20" aria-hidden="true"><path d="M5 1.5l3 4-2 2.2c1 2.3 2.8 4.1 5.2 5.2l2.2-2 4 3-1.6 3.3C9 17 3 11 1.8 3.2z"/></svg>
        406-555-8142
      </li>
      <li>
        <svg viewBox="0 0 20 20" aria-hidden="true"><path d="M1 4h18v12H1z M2.5 5.5l7.5 6 7.5-6" fill="none" stroke="#5a5a5a" stroke-width="1.6"/></svg>
        dwight@kestrelmoorbuilders.com
      </li>
    </ul>
  </section>

  <section class="card card--front" aria-label="Business card, front side">
    <p class="company-name front-name">
      <span class="company-name__main">Kestrelmoor</span>
      <span class="company-name__sub">Builders LLC.</span>
    </p>
    <div class="front-stripe front-stripe--one"></div>
    <div class="front-stripe front-stripe--two"></div>
  </section>

</main>
</body>
</html>
```